Business Card Design for a Jockey's Agent

A business card design that helps to develop a brand or identity for myself, the agent, perhaps on one side with a clean minimalist design, and on the other side a simple design with the two jockeys names i currently represent. Those jockeys may change twice a year as they move around the country, switch agents, etc, so i think keeping one side designed to promote the agent and a second side that can be changed easily to identify the jockeys i currently represent would be the best.

Target Market(s)

Thoroughbred racehorse trainers

Industry/Entity Type

Business

Contact Information for Business Card

Garrett Lindqvist - Jockey Agent
mobile (614) 382 7291
garrettplindqvist7mailhub.example

Jockeys: Everett Kline, Tobias Renwick

Font styles to use
Serif

Requirements
Must have
• contact info and modern feel and font
Nice to have
• clean minimalist element of racing, jockey silk, helmut or crop, finish marker pole from racetrack etc,
Should not have
• DONT HAVE ANY KIND OF LOGO ETC. IMAGE IS ONE OF MY RACEHORSES TO HELP FINISH BRIEF.
• racing horse, stuffy vintage racing feel or Weekly Paddock Sheet fonts

```html
<!DOCTYPE html>
<html lang="en">
<head>
<meta charset="utf-8">
<title>Garrett Lindqvist — Jockey Agent Business Card</title>
<link rel="stylesheet" href="https://fonts.googleapis.com/css2?family=Montserrat:wght@400;500;600&family=Mulish:wght@400&display=swap">
<style>
  :root {
    --page-bg: #d9d9d9;
    --card-paper: #efefef;
    --brand-brown: #a65a08;
    --brand-orange: #e98a24;
    --photo-dark: #333333;
    --ink: #2a2a2a;
    --label-white: #f7f7f7;
    --label-tint: #f7c98f;
  }
  * { margin: 0; padding: 0; box-sizing: border-box; }
  html, body { width: 1200px; height: 1200px; overflow: hidden; }
  body {
    background: var(--page-bg);
    font-family: "Montserrat", Arial, sans-serif;
    position: relative;
  }
  .card {
    position: absolute;
    left: 150px;
    width: 900px;
    height: 514px;
    background: var(--card-paper);
    overflow: hidden;
    box-shadow: 0 10px 30px rgba(0,0,0,0.18);
  }
  .card--front { top: 60px; }
  .card--back { top: 626px; }
  .card__art { position: absolute; inset: 0; width: 100%; height: 100%; }

  .agent-name {
    position: absolute;
    left: 70px;
    top: 150px;
    color: var(--brand-brown);
    font-weight: 600;
    font-size: 64px;
    line-height: 0.95;
    letter-spacing: 1px;
    text-transform: uppercase;
  }
  .agent-title {
    position: absolute;
    left: 74px;
    top: 283px;
    color: var(--ink);
    font-weight: 500;
    font-size: 22px;
    letter-spacing: 1px;
    text-transform: uppercase;
  }
  .contact-list {
    position: absolute;
    left: 84px;
    top: 345px;
    list-style: none;
    font-family: "Mulish", Arial, sans-serif;
    color: var(--ink);
    font-size: 26px;
  }
  .contact-list li {
    display: flex;
    align-items: center;
    gap: 16px;
    margin-bottom: 10px;
  }
  .contact-list svg { width: 30px; height: 30px; flex: none; }

  .jockey-label {
    position: absolute;
    background: var(--label-white);
    color: var(--ink);
    font-weight: 500;
    font-size: 24px;
    text-transform: uppercase;
    padding: 12px 22px 10px 34px;
    box-shadow: 8px -8px 0 var(--label-tint);
    white-space: nowrap;
  }
  .jockey-label--first { left: 320px; top: 145px; }
  .jockey-label--second { left: 560px; top: 255px; }
</style>
</head>
<body>

  <section class="card card--front" aria-label="Agent side">
    <svg class="card__art" viewBox="0 0 900 514" aria-hidden="false">
      <polygon class="panel-edge" points="555,0 900,0 900,514 820,514 580,300 555,300" fill="var(--brand-brown)"/>
      <polygon class="panel-photo" points="568,0 900,0 900,514 838,514 594,290 568,290" fill="var(--photo-dark)" role="img" aria-label="Darkened photograph of the agent's racehorse"/>
    </svg>
    <h1 class="agent-name">Garrett<br>Lindqvist</h1>
    <p class="agent-title">Jockey Agent</p>
    <ul class="contact-list">
      <li>
        <svg viewBox="0 0 24 24" aria-hidden="true"><path fill="var(--brand-brown)" d="M6.6 10.8a15 15 0 0 0 6.6 6.6l2.2-2.2c.3-.3.7-.4 1-.2 1.1.4 2.3.6 3.6.6.6 0 1 .4 1 1V20c0 .6-.4 1-1 1A17 17 0 0 1 3 4c0-.6.4-1 1-1h3.5c.6 0 1 .4 1 1 0 1.3.2 2.5.6 3.6.1.3 0 .7-.2 1z"/></svg>
        <span>(614) 382 7291</span>
      </li>
      <li>
        <svg viewBox="0 0 24 24" aria-hidden="true"><rect x="2" y="5" width="20" height="14" fill="var(--brand-brown)"/><path d="M2 5l10 8 10-8" fill="none" stroke="var(--card-paper)" stroke-width="1.6"/></svg>
        <span>garrettplindqvist7mailhub.example</span>
      </li>
    </ul>
  </section>

  <section class="card card--back" aria-label="Jockeys side">
    <svg class="card__art" viewBox="0 0 900 514">
      <polygon class="panel-edge" points="160,0 900,0 900,514 440,514 190,380 175,380" fill="var(--brand-brown)"/>
      <polygon class="panel-photo" points="172,0 900,0 900,514 462,514 200,370 186,370" fill="var(--brand-orange)" role="img" aria-label="Orange-toned photograph of a racehorse at the track"/>
      <g class="jockey-pin" transform="translate(270,205)">
        <path d="M-60,-5 A62,62 0 1 1 55,30 L60,95 L-30,55 A62,62 0 0 1 -60,-5 Z" fill="var(--brand-brown)"/>
        <circle r="50" fill="var(--card-paper)"/>
        <circle cx="0" cy="-14" r="17" fill="var(--brand-brown)"/>
        <path d="M-30,28 Q-30,2 0,6 Q30,2 30,28 Z" fill="var(--brand-brown)"/>
      </g>
      <g class="jockey-pin" transform="translate(510,315)">
        <path d="M-60,-5 A62,62 0 1 1 55,30 L60,95 L-30,55 A62,62 0 0 1 -60,-5 Z" fill="var(--brand-brown)"/>
        <circle r="50" fill="var(--card-paper)"/>
        <circle cx="0" cy="-14" r="17" fill="var(--brand-brown)"/>
        <path d="M-30,28 Q-30,2 0,6 Q30,2 30,28 Z" fill="var(--brand-brown)"/>
      </g>
    </svg>
    <p class="jockey-label jockey-label--first">Everett Kline</p>
    <p class="jockey-label jockey-label--second">Tobias Renwick</p>
  </section>

</body>
</html>
```